Rack Card for Portuguese Walking Food Tour

I would like a vertical rack card measuring 99x210mm. Here is the information I would like to include. It does not need to be in this format. We are located in Setubal, Portugal.
Please use the attached Teal Heron Logo.
Setúbal: Tradition and Today
Experience the culinary delights of Setúbal, Portugal with a walking food tour around our waterfront village. Discover the Mercado da Gaivota Branca, voted one of the world’s best markets by Metro Ledger, and indulge in local wines and dishes. Prepare for a calm stroll on flat streets. No hills to climb on this tour.
Duration: 4 hours
www.brinebasketwalks.com
+351 265 000 487

```html
<!DOCTYPE html>
<html lang="en">
<head>
<meta charset="utf-8">
<title>Brine Basket Walks – Setúbal Rack Card</title>
<link rel="stylesheet" href="https://fonts.googleapis.com/css2?family=Poppins:wght@600;700&display=swap">
<style>
  :root {
    --paper: #ffffff;
    --brand-orange: #f26522;
    --ink-light: #ffffff;
    --shadow-ellipse: #e8845a;
    --fish-pink: #e9a49a;
    --fish-red: #d9563f;
    --fish-cream: #f1ddd3;
    --fish-gold: #e3a646;
  }
  * { margin: 0; padding: 0; box-sizing: border-box; }
  html, body {
    width: 1200px; height: 2453px; overflow: hidden;
    background: var(--paper);
    font-family: "Poppins", sans-serif;
  }
  .rack-card {
    position: relative; width: 1200px; height: 2453px;
    background: var(--paper);
  }
  .card-panel {
    position: absolute; left: 43px; top: 45px;
    width: 1112px; height: 2361px;
    background: var(--brand-orange);
  }
  .brand {
    position: absolute; left: 230px; top: 165px;
    display: flex; align-items: center; gap: 34px;
    color: var(--ink-light); font-weight: 700;
  }
  .brand-dot {
    width: 150px; height: 150px; border-radius: 50%;
    background: var(--ink-light); flex: none;
  }
  .brand-name { line-height: 1; }
  .brand-name .main { display: block; font-size: 86px; letter-spacing: -1px; }
  .brand-name .sub { display: block; font-size: 46px; letter-spacing: 10px; margin-top: 10px; padding-left: 240px; }
  .headline {
    position: absolute; left: 114px; top: 512px;
    font-size: 64px; font-weight: 600; color: var(--ink-light);
    white-space: nowrap; letter-spacing: -0.3px;
  }
  .intro {
    position: absolute; left: 127px; top: 628px; width: 980px;
    font-size: 50.5px; line-height: 63.3px; font-weight: 600;
    color: var(--ink-light); letter-spacing: -0.2px;
  }
  .duration {
    position: absolute; left: 171px; top: 1300px;
    font-size: 61px; font-weight: 600; color: var(--ink-light);
  }
  .contact {
    position: absolute; left: 166px; display: flex; align-items: center;
    color: var(--ink-light); font-weight: 600; white-space: nowrap;
  }
  .contact svg { flex: none; }
  .contact-web { top: 1410px; gap: 28px; font-size: 54px; }
  .contact-phone { top: 1518px; gap: 30px; font-size: 72px; letter-spacing: -1px; }
  .market-photo { position: absolute; left: 0; top: 0; }
</style>
</head>
<body>
<main class="rack-card">
  <div class="card-panel"></div>

  <header class="brand" aria-label="Brine Basket Walks">
    <span class="brand-dot"></span>
    <span class="brand-name">
      <span class="main">Brine Basket</span>
      <span class="sub">WALKS</span>
    </span>
  </header>

  <h1 class="headline">Setúbal: Tradition and Today</h1>

  <p class="intro">Experience the culinary delights of Setúbal, Portugal with a walking food tour around our waterfront village. Discover the Mercado da Gaivota Branca, voted one of the world’s best markets by Metro Ledger, and indulge in local wines and dishes. Prepare for a calm stroll on flat streets. No hills to climb on this tour.</p>

  <p class="duration">Duration: 4 hours</p>

  <p class="contact contact-web">
    <svg width="74" height="74" viewBox="0 0 74 74" aria-hidden="true" fill="none" stroke="#fff" stroke-width="4">
      <circle cx="34" cy="34" r="30"/>
      <ellipse cx="34" cy="34" rx="13" ry="30"/>
      <line x1="4" y1="34" x2="64" y2="34"/>
      <path d="M9 19 H59 M9 49 H59"/>
      <path d="M46 46 L70 56 L59 59 L67 70 L62 73 L55 62 L48 70 Z" fill="#fff" stroke="var(--brand-orange)" stroke-width="3"/>
    </svg>
    <span>www.brinebasketwalks.com</span>
  </p>

  <p class="contact contact-phone">
    <svg width="74" height="74" viewBox="0 0 74 74" aria-hidden="true">
      <path d="M14 6 L26 6 L30 22 L22 28 Q28 42 44 50 L50 42 L66 46 L66 58 Q62 70 50 68 Q18 60 6 24 Q6 10 14 6 Z" fill="#fff"/>
      <path d="M42 20 Q52 22 54 32 M44 8 Q64 12 66 30" fill="none" stroke="#fff" stroke-width="5" stroke-linecap="round"/>
    </svg>
    <span>+351 265 000 487</span>
  </p>

  <svg class="market-photo" width="1200" height="2453" viewBox="0 0 1200 2453" role="img" aria-label="Photograph of fresh red mullet piled on a fish market stall">
    <defs>
      <linearGradient id="fishTones" x1="0" y1="0" x2="1" y2="1">
        <stop offset="0" stop-color="var(--fish-red)"/>
        <stop offset="0.35" stop-color="var(--fish-pink)"/>
        <stop offset="0.6" stop-color="var(--fish-cream)"/>
        <stop offset="0.8" stop-color="var(--fish-gold)"/>
        <stop offset="1" stop-color="var(--fish-red)"/>
      </linearGradient>
    </defs>
    <polygon fill="#fff" points="43,2028 67,1961 95,1923 152,1866 200,1828 228,1752 214,1733 276,1685 324,1690 343,1704 571,1690 704,1685 743,1704 876,1714 914,1723 981,1742 1019,1809 1066,1842 1119,1866 1155,2028 1155,2406 43,2406"/>
    <polygon fill="url(#fishTones)" points="43,2045 76,1972 105,1935 162,1878 212,1840 242,1764 238,1745 282,1702 322,1706 345,1720 571,1704 702,1700 740,1718 874,1728 910,1737 972,1756 1008,1820 1058,1855 1108,1878 1155,2045 1155,2406 43,2406"/>
  </svg>
</main>
</body>
</html>
```